Clara Joy Halden- Lantern Waltz- Autumn/Winter Tour Dates

I need high res A3 Tour poster for print and for social media JPG sharing of tour dates.
Also needed Facebook/Twitter Banner Cover Photos of these dates.
Text Needed Below
Clara Joy Halden
Lantern Waltz
Autumn/Winter Tour Dates
03/09 Ravensby Folk Festival
21/09 Swindon- Calder Theatre
01/10 Hitchin- Brackwell Folk Club
17/10 Bath- The Anvil
20/10 Sheffield- Upper Dale Croquet Club
24/10 Birmingham- Orchard Lamp Cafe
26/10 Glasgow- The Nook and Jar
27/10 Edinburgh - The Marble Parlour
08/11 Capital Reel and Ballad Festival- The Crooked Heron
25/11 Lewes- Tandem Record Shop- Live In Store
02/12 Cambridge- The Quayside
27/01 Lincolnshire- Fenmarsh Theatre
Tickets/Info: www.clarajoyhalden-music.example/gigs
(Quotes/Reviews To Put On)
"Outstanding, rich and expressive."            "Vibrant and Experimental"
**** BdM                                                               **** Tunepaths
"Impressive and Invigorating"                        "Enchanting" Acoustic Wire UK
tBarks

Updates
I cannot read the tour dates on most of the submissions so far. They need to be visible to viewers.
Thank You.
Please also be as creative and inventive as possible- not bland.

Target Market(s)
Music Fans- Folk Acoustic Americana
Industry/Entity Type
Media
Font styles to use
Requirements
Must have
- My photo featured prominently
- Look classy and not tacky or OTT
- Look elegant, wintery and eye catching
- The dates must be very clear to read
- Links to Website:

Nice to have
- Something innovative and not boring in terms of layout design
- Perhaps fading/ misty or wintery

Should not have
- Any colours that do not match

```html
<!DOCTYPE html>
<html lang="en">
<head>
<meta charset="utf-8">
<title>Clara Joy Halden – Lantern Waltz Tour Poster</title>
<link rel="stylesheet" href="https://fonts.googleapis.com/css2?family=Open+Sans:wght@600;700&family=Playfair+Display:wght@500;600&display=swap">
<style>
  :root {
    --night: #1f2733;
    --slate: #3c4a5e;
    --dusk: #5d7690;
    --mist: #9cc0d6;
    --ice: #c9e2ef;
    --frost: #e4f1f8;
    --ink: #1d2836;
    --snow: #ffffff;
  }
  html, body { margin: 0; padding: 0; overflow: hidden; }
  body { width: 849px; height: 1200px; background: var(--frost); }
  .poster {
    position: relative;
    width: 849px;
    height: 1200px;
    overflow: hidden;
    background: linear-gradient(180deg, var(--mist) 0%, var(--ice) 60%, var(--frost) 100%);
  }
  .portrait {
    position: absolute;
    left: 110px; top: 0;
    width: 630px; height: 700px;
    background:
      radial-gradient(ellipse 190px 240px at 50% 45%, #c7ccd8 0%, #8a93a6 35%, rgba(60,72,92,0) 75%),
      radial-gradient(ellipse 340px 420px at 50% 40%, #232a36 40%, rgba(35,42,54,0) 100%),
      linear-gradient(180deg, #2b3442 0%, #3a4657 55%, #6d88a2 85%, rgba(156,192,214,0) 100%);
    -webkit-mask-image: linear-gradient(90deg, transparent 0%, #000 12%, #000 88%, transparent 100%);
            mask-image: linear-gradient(90deg, transparent 0%, #000 12%, #000 88%, transparent 100%);
  }
  .frost-edge {
    position: absolute;
    top: 0; bottom: 0;
    width: 160px;
  }
  .frost-edge.left {
    left: 0;
    background:
      linear-gradient(180deg, rgba(228,241,248,0.2) 0%, rgba(228,241,248,0) 40%),
      linear-gradient(90deg, #b4d3e5 0%, #a6c8dc 45%, rgba(166,200,220,0) 100%);
  }
  .frost-edge.right {
    right: 0;
    background:
      linear-gradient(180deg, rgba(228,241,248,0.2) 0%, rgba(228,241,248,0) 40%),
      linear-gradient(270deg, #b4d3e5 0%, #a6c8dc 45%, rgba(166,200,220,0) 100%);
  }
  .snowfall {
    position: absolute;
    left: 0; right: 0;
    top: 560px; height: 220px;
    background: linear-gradient(180deg, rgba(201,226,239,0) 0%, rgba(201,226,239,0.75) 45%, rgba(214,233,243,0.9) 70%, rgba(214,233,243,0) 100%);
  }
  .artist, .album {
    position: absolute;
    left: 0; right: 0;
    margin: 0;
    text-align: center;
    color: var(--snow);
    font-family: "Playfair Display", serif;
    text-shadow: 0 1px 6px rgba(20,28,40,0.35);
  }
  .artist { top: 520px; font-size: 38px; font-weight: 600; letter-spacing: 0.3px; }
  .album { top: 590px; font-size: 62px; font-weight: 500; letter-spacing: 1px; line-height: 1; }
  .tour {
    position: absolute;
    left: 162px; top: 680px;
    color: var(--ink);
    font-family: "Open Sans", sans-serif;
  }
  .tour-heading { margin: 0 0 4px; font-size: 16px; font-weight: 700; line-height: 24px; }
  .dates { list-style: none; margin: 0; padding: 0; }
  .dates li { font-size: 17px; font-weight: 700; line-height: 25.6px; white-space: nowrap; }
  .dates .day { display: inline-block; width: 65px; font-size: 16px; }
  .dates .venue { font-variant: small-caps; letter-spacing: 0.2px; }
  .dates .venue.plain { font-variant: normal; font-weight: 600; font-size: 16px; letter-spacing: 0; }
  .tickets {
    position: absolute;
    left: 162px; top: 1041px;
    margin: 0;
    font-family: "Open Sans", sans-serif;
    font-size: 16px; font-weight: 700; line-height: 24px;
    color: var(--ink);
  }
  .reviews {
    position: absolute;
    left: 258px; top: 1078px;
    margin: 0; padding: 0; list-style: none;
    font-family: "Open Sans", sans-serif;
    font-size: 14px; font-weight: 600; line-height: 25px;
    color: var(--ink);
  }
</style>
</head>
<body>
<main class="poster">
  <div class="portrait" role="img" aria-label="Portrait photograph of the singer wearing a pearl-wire crown, set in a dark snowy winter forest"></div>
  <div class="frost-edge left" role="img" aria-label="Frosted bare birch trees fading into winter mist"></div>
  <div class="frost-edge right" role="img" aria-label="Frosted bare birch trees fading into winter mist"></div>
  <div class="snowfall" role="img" aria-label="Drifting snow flurry with pale snowflakes"></div>

  <h1 class="artist">Clara Joy Halden</h1>
  <h2 class="album">Lantern Waltz</h2>

  <section class="tour">
    <h3 class="tour-heading">AUTUMN/WINTER TOUR DATES</h3>
    <ul class="dates">
      <li><span class="day">03/09</span><span class="venue">Ravensby Folk Festival</span></li>
      <li><span class="day">21/09</span><span class="venue">Swindon- Calder Theatre</span></li>
      <li><span class="day">01/10</span><span class="venue">Hitchin- Brackwell Folk Club</span></li>
      <li><span class="day">17/10</span><span class="venue">Bath, The Anvil</span></li>
      <li><span class="day">20/10</span><span class="venue">Sheffield, Upper Dale Croquet Club</span></li>
      <li><span class="day">24/10</span><span class="venue">Birmingham- Orchard Lamp Cafe</span></li>
      <li><span class="day">26/10</span><span class="venue">Glasgow, The Nook and Jar</span></li>
      <li><span class="day">27/10</span><span class="venue">Edinburgh - The Marble Parlour</span></li>
      <li><span class="day">08/11</span><span class="venue">Capital Reel and Ballad Festival- The Crooked Heron</span></li>
      <li><span class="day">25/11</span><span class="venue">Lewes- Tandem Record Shop- Live In Store</span></li>
      <li><span class="day">02/12</span><span class="venue plain">Cambridge- The Quayside</span></li>
      <li><span class="day">27/01</span><span class="venue plain">Lincolnshire- Fenmarsh Theatre</span></li>
    </ul>
  </section>

  <p class="tickets">Tickets/Info: www.clarajoyhalden-music.example/gigs</p>

  <ul class="reviews">
    <li>"Outstanding, rich and expressive."&nbsp; - BdM</li>
    <li>"Vibrant and Experimental" -&nbsp; Tunepaths</li>
    <li>"Impressive and Invigorating" - Acoustic Wire</li>
    <li>"Enchanting" - UK tBarks</li>
  </ul>
</main>
</body>
</html>
```